Criação de Papelaria Profissional para Advocacia e Direito
A empresa queria:
" Somos um escritório de advocacia full-service, com sede em Santarém-PA e uma unidade em Manaus-AM. Temos atuação em todo o Brasil. "

```html
<!DOCTYPE html>
<html lang="pt-BR">
<head>
<meta charset="utf-8">
<title>Pasta Institucional – Moreira Vidal Advogados Associados</title>
<link rel="stylesheet" href="https://fonts.googleapis.com/css2?family=Cinzel:wght@400;500&family=Lato:wght@400;700&display=swap">
<style>
  :root {
    --backdrop: #efeeea;
    --cream: #f6f3ec;
    --paper: #fbfaf7;
    --navy: #0f2c4c;
    --navy-deep: #0a223d;
    --copper: #d5a98f;
    --gold: #c9a98a;
    --ink: #4a4a4a;
    --watermark: #ece3d6;
  }
  * { margin: 0; padding: 0; box-sizing: border-box; }
  html, body { width: 1200px; height: 1200px; overflow: hidden; }
  body { background: var(--backdrop); font-family: "Lato", sans-serif; position: relative; }

  .folder { position: absolute; left: 0; top: 0; width: 1200px; height: 1200px; }

  .pocket-sheet {
    position: absolute; left: 560px; top: 300px; width: 500px; height: 640px;
    background: var(--paper);
  }
  .pocket-sheet .pocket-curve {
    position: absolute; right: 0; bottom: 0; width: 240px; height: 260px;
    background: var(--copper); border-top-left-radius: 240px 260px;
  }
  .pocket-lower {
    position: absolute; left: 150px; top: 760px; width: 410px; height: 180px;
    background: var(--paper); border-top: 1px solid #e6e3dc;
  }

  .inside-cover {
    position: absolute; left: 150px; top: 180px; width: 410px; height: 580px;
    background: var(--cream);
  }
  .inside-cover .watermark-area {
    position: absolute; left: 20px; top: 20px; width: 320px; height: 420px;
    background: radial-gradient(ellipse at 45% 45%, var(--watermark) 0%, rgba(236,227,214,0.4) 55%, rgba(246,243,236,0) 75%);
  }
  .contact-band {
    position: absolute; left: 28px; bottom: 30px; right: 24px;
    display: flex; gap: 22px; align-items: flex-start;
  }
  .contact-band .firm-mini {
    font-family: "Cinzel", serif; font-size: 9px; color: var(--navy);
    letter-spacing: 0.5px; text-align: center; width: 90px; line-height: 1.3;
  }
  .contact-band .firm-mini .mark { display: block; width: 12px; height: 12px; margin: 0 auto 4px; background: var(--gold); }
  .contact-col { font-size: 6.5px; color: var(--ink); line-height: 1.6; }
  .contact-col .office { font-weight: 700; color: var(--navy); }

  .front-cover {
    position: absolute; left: 560px; top: 180px; width: 410px; height: 580px;
    background: linear-gradient(160deg, var(--navy) 0%, var(--navy-deep) 100%);
    overflow: hidden;
  }
  .front-cover .deco-area {
    position: absolute; left: 40px; top: 40px; width: 340px; height: 520px;
    background: linear-gradient(150deg, rgba(255,255,255,0.05), rgba(255,255,255,0) 70%);
  }
  .brand {
    position: absolute; left: 0; right: 0; top: 170px; text-align: center; color: var(--gold);
  }
  .brand .mark { display: block; width: 34px; height: 34px; margin: 0 auto 16px; background: var(--gold); }
  .brand .name { font-family: "Cinzel", serif; font-size: 25px; letter-spacing: 1px; font-weight: 400; }
  .brand .tagline {
    display: flex; align-items: center; justify-content: center; gap: 8px;
    font-family: "Cinzel", serif; font-size: 8px; letter-spacing: 2px; margin-top: 6px;
  }
  .brand .tagline::before, .brand .tagline::after {
    content: ""; width: 34px; height: 1px; background: var(--gold);
  }
</style>
</head>
<body>
  <main class="folder">
    <div class="pocket-sheet"><div class="pocket-curve"></div></div>
    <div class="pocket-lower"></div>

    <section class="inside-cover">
      <div class="watermark-area" role="img" aria-label="Faint large firm emblem decoration"></div>
      <div class="contact-band">
        <div class="firm-mini"><span class="mark"></span>Moreira Vidal</div>
        <div class="contact-col">
          <div class="office">Unidade Santarém</div>
          <div>(93) 3500-0000</div>
          <div>contato@moreiravidal.adv.br</div>
          <div>Av. Central, 1200 – Centro</div>
          <div>Santarém – PA</div>
        </div>
        <div class="contact-col">
          <div class="office">Unidade Manaus</div>
          <div>(92) 3600-0000</div>
          <div>manaus@moreiravidal.adv.br</div>
          <div>Rua das Flores, 45 – Centro</div>
          <div>Manaus – AM</div>
        </div>
      </div>
    </section>

    <section class="front-cover">
      <div class="deco-area" role="img" aria-label="Subtle large emblem decoration in navy tones"></div>
      <div class="brand">
        <span class="mark"></span>
        <div class="name">MOREIRA VIDAL</div>
        <div class="tagline">ADVOGADOS ASSOCIADOS</div>
      </div>
    </section>
  </main>
</body>
</html>
```